Special release wine label

Marrow Creek Vineyards is a small premium wine producer in the Barossa - South Australia. We are a five star rated winery, producing exceptional wines true to variety, region and house style. We have a very special parcel of wine that we wish to release as an exclusive wine. Visit www.marrowcreekvineyards.com.au for further feel.

The wine will be called Marrow Creek Vineyards, 2012, The Quiet Harvest Shiraz - Cabernet.

The wine can be bottled in either a burgundy or Bordeaux shaped bottle

Industry/Entity Type

House

```html
<!DOCTYPE html>
<html lang="en">
<head>
<meta charset="utf-8">
<title>Marrow Creek Vineyards – The Quiet Harvest Shiraz - Cabernet 2012</title>
<link rel="stylesheet" href="https://fonts.googleapis.com/css2?family=Marcellus+SC&family=Montserrat:wght@500&family=Playfair+Display:wght@900&display=swap">
<style>
  :root {
    --page: #ffffff;
    --label-black: #0d0d0d;
    --label-charcoal: #2a2a2a;
    --gold-light: #fff3b0;
    --gold-mid: #e2b54a;
    --gold-deep: #8a5a12;
    --sky-top: #f2b24a;
    --sky-low: #d9c79a;
    --field-olive: #6b6a4e;
    --name-strip: #5c5a44;
    --cream: #fbf1d8;
    --tan: #d4a868;
    --white: #ffffff;
  }
  * { margin: 0; padding: 0; box-sizing: border-box; }
  html, body {
    width: 1200px;
    height: 999px;
    overflow: hidden;
    background: var(--page);
  }
  .label {
    position: absolute;
    left: 380px;
    top: 80px;
    width: 440px;
    height: 840px;
  }
  .vintage {
    font-family: "Playfair Display", Georgia, serif;
    font-weight: 900;
    font-size: 40px;
  }
  .estate-name {
    font-family: "Montserrat", Arial, sans-serif;
    font-weight: 500;
    font-size: 27px;
    letter-spacing: 1.5px;
  }
  .wine-name {
    font-family: "Marcellus SC", Georgia, serif;
    font-size: 33px;
    letter-spacing: 0.5px;
  }
</style>
</head>
<body>
<svg class="label" viewBox="0 0 440 840" xmlns="http://www.w3.org/2000/svg">
  <defs>
    <linearGradient id="gold-frame" x1="0" y1="0" x2="1" y2="1">
      <stop offset="0" stop-color="var(--gold-light)"/>
      <stop offset="0.35" stop-color="var(--gold-mid)"/>
      <stop offset="0.6" stop-color="var(--gold-deep)"/>
      <stop offset="0.85" stop-color="var(--gold-mid)"/>
      <stop offset="1" stop-color="var(--gold-light)"/>
    </linearGradient>
    <linearGradient id="gold-type" x1="0" y1="0" x2="0" y2="1">
      <stop offset="0" stop-color="var(--gold-light)"/>
      <stop offset="0.55" stop-color="var(--gold-mid)"/>
      <stop offset="1" stop-color="var(--gold-deep)"/>
    </linearGradient>
    <linearGradient id="label-field" x1="0" y1="0" x2="1" y2="0">
      <stop offset="0" stop-color="var(--label-black)"/>
      <stop offset="0.5" stop-color="var(--label-charcoal)"/>
      <stop offset="1" stop-color="var(--label-black)"/>
    </linearGradient>
    <linearGradient id="vineyard-scene" x1="0" y1="0" x2="0" y2="1">
      <stop offset="0" stop-color="var(--sky-top)"/>
      <stop offset="0.55" stop-color="var(--sky-low)"/>
      <stop offset="1" stop-color="var(--field-olive)"/>
    </linearGradient>
    <radialGradient id="medallion-face" cx="0.45" cy="0.4" r="0.65">
      <stop offset="0" stop-color="var(--cream)"/>
      <stop offset="1" stop-color="var(--tan)"/>
    </radialGradient>
  </defs>

  <!-- label outline with arched crown -->
  <path class="label-frame" fill="url(#gold-frame)"
        d="M0,160 Q0,115 45,110 Q118,104 138,48 Q156,4 220,4 Q284,4 302,48 Q322,104 395,110 Q440,115 440,160 L440,720 Q440,770 390,770 L50,770 Q0,770 0,720 Z"/>
  <path class="label-field" fill="url(#label-field)"
        d="M12,165 Q12,126 50,122 Q128,114 150,56 Q166,18 220,18 Q274,18 290,56 Q312,114 390,122 Q428,126 428,165 L428,716 Q428,758 388,758 L52,758 Q12,758 12,716 Z"/>

  <!-- vintage -->
  <text class="vintage" x="220" y="86" text-anchor="middle" fill="url(#gold-type)">2012</text>

  <!-- estate artwork panel -->
  <rect x="56" y="112" width="328" height="312" fill="var(--name-strip)"/>
  <rect x="66" y="122" width="308" height="230" fill="url(#vineyard-scene)"
        role="img" aria-label="Sketch of the homestead cottage framed by tall palm trees and a cypress under a golden sunset sky"/>
  <text class="estate-name" x="220" y="398" text-anchor="middle" fill="var(--white)">MARROW CREEK</text>

  <!-- wine name -->
  <text class="wine-name" x="220" y="488" text-anchor="middle" fill="url(#gold-type)">The Quiet Harvest</text>
  <text class="wine-name" x="220" y="536" text-anchor="middle" fill="url(#gold-type)">Shiraz - Cabernet</text>

  <!-- grape medallion -->
  <circle cx="220" cy="690" r="138" fill="url(#gold-frame)"/>
  <circle cx="220" cy="690" r="124" fill="url(#medallion-face)"
          role="img" aria-label="Engraved grape bunch with vine leaves"/>
</svg>
</body>
</html>
```